Stationary Design for Stunning new Logo

I need to envelopes, letterhead, business cards designed to compliment our new logo.

We are a 25 year old printing company going through a brand refresh. All items should have the design extended to both sides for full print ability.

Industry/Entity Type

Printing

Requirements
Must have
• It must utilize the new logo & colors PMS 300 & PMS 295.

```html
<!DOCTYPE html>
<html lang="en">
<head>
<meta charset="utf-8">
<title>Crestprint Stationery</title>
<link href="https://fonts.googleapis.com/css2?family=Open+Sans:ital,wght@0,400;0,600;0,700;1,400&display=swap" rel="stylesheet">
<style>
  :root {
    --navy: #0b3f7a;
    --navy-deep: #062c5c;
    --blue: #1266bf;
    --blue-light: #2f86d8;
    --paper: #ffffff;
    --ink: #5a6470;
    --backdrop: #eceef1;
  }
  * { box-sizing: border-box; margin: 0; padding: 0; }
  html, body { width: 1200px; height: 900px; overflow: hidden; }
  body {
    background: var(--backdrop);
    font-family: "Open Sans", Arial, sans-serif;
    color: var(--ink);
    position: relative;
  }
  .sheet { position: absolute; box-shadow: 0 4px 14px rgba(0,0,0,.18); overflow: hidden; }

  .brand { display: flex; align-items: center; gap: 6px; }
  .brand-dot { border-radius: 50%; background: var(--blue); flex: none; }
  .brand-name { font-weight: 700; color: var(--navy); letter-spacing: .02em; line-height: 1; white-space: nowrap; }
  .brand-tag { font-size: 6px; color: var(--blue); letter-spacing: .06em; text-transform: uppercase; margin-top: 3px; white-space: nowrap; }
  .on-dark .brand-dot { background: #fff; }
  .on-dark .brand-name, .on-dark .brand-tag { color: #fff; }

  /* Folder */
  .folder {
    left: 60px; top: 40px; width: 340px; height: 480px;
    background: linear-gradient(160deg, var(--navy) 0%, var(--navy-deep) 100%);
  }
  .folder .brand-block { position: absolute; right: 26px; bottom: 34px; }
  .folder .brand-dot { width: 16px; height: 16px; }
  .folder .brand-name { font-size: 22px; }

  /* Letterhead */
  .letterhead { left: 430px; top: 40px; width: 340px; height: 480px; background: var(--paper); }
  .letterhead .brand-block { position: absolute; left: 20px; top: 28px; width: 150px; }
  .letterhead .brand-dot { width: 10px; height: 10px; }
  .letterhead .brand-name { font-size: 14px; }
  .letterhead .brand-tag { font-size: 4.6px; letter-spacing: .04em; }
  .contact-block {
    position: absolute; left: 186px; right: 14px; top: 30px; display: flex; gap: 7px;
    font-size: 5.5px; line-height: 1.55; white-space: nowrap;
  }
  .contact-block .divider { width: 1px; background: var(--navy); flex: none; }
  .contact-line { display: flex; align-items: center; gap: 3px; white-space: nowrap; }
  .contact-icon { width: 5px; height: 5px; border-radius: 50%; background: var(--blue); flex: none; }
  .contact-block .contact-icon { width: 4px; height: 4px; }
  .footer-wave { position: absolute; left: 0; bottom: 0; width: 100%; }
  .web { position: absolute; color: #fff; font-size: 7px; font-style: italic; white-space: nowrap; }
  .letterhead .web { right: 24px; bottom: 10px; }

  /* Envelope */
  .envelope { left: 60px; top: 560px; width: 710px; height: 300px; background: var(--paper); }
  .envelope .flap { position: absolute; left: 0; top: 0; width: 100%; }
  .envelope .brand-block { position: absolute; left: 30px; top: 74px; }
  .envelope .brand-dot { width: 16px; height: 16px; }
  .envelope .brand-name { font-size: 22px; }
  .envelope .brand-tag { font-size: 7px; }
  .address-window {
    position: absolute; left: 40px; top: 150px; width: 230px; height: 70px;
    border: 1px solid #c9ced4; border-radius: 10px;
    background: linear-gradient(180deg, #f4f5f7, #dfe2e6);
  }
  .envelope .return-address {
    position: absolute; right: 50px; bottom: 34px; font-size: 9px; line-height: 1.5; font-style: italic;
  }
  .envelope .contact-icon { width: 6px; height: 6px; }

  /* Business cards */
  .card { width: 320px; height: 183px; border-radius: 14px; }
  .card-front { left: 820px; top: 80px; background: var(--paper); }
  .card-front .brand-block { position: absolute; left: 18px; top: 18px; }
  .card-front .brand-dot { width: 13px; height: 13px; }
  .card-front .brand-name { font-size: 19px; }
  .person { position: absolute; left: 22px; top: 66px; font-size: 7px; line-height: 1.5; }
  .person-name { font-size: 9px; font-weight: 700; color: var(--navy); text-transform: uppercase; white-space: nowrap; }
  .person-name span { font-weight: 400; text-transform: none; color: var(--blue); }
  .card-front .divider { position: absolute; left: 164px; top: 80px; width: 1px; height: 44px; background: var(--navy); }
  .card-front .address { position: absolute; left: 176px; top: 82px; font-size: 7px; line-height: 1.5; font-style: italic; white-space: nowrap; }
  .card-front .web { right: 18px; bottom: 8px; font-size: 7px; }

  .card-back {
    left: 820px; top: 320px;
    background: linear-gradient(160deg, var(--navy) 0%, var(--navy-deep) 100%);
    display: flex; align-items: center; justify-content: center;
  }
  .card-back .brand-dot { width: 16px; height: 16px; }
  .card-back .brand-name { font-size: 24px; }
  .card-back .web { left: 0; right: 0; bottom: 12px; text-align: center; font-size: 6.5px; opacity: .8; }
</style>
</head>
<body>

  <!-- Presentation folder -->
  <section class="sheet folder on-dark">
    <div class="brand-block">
      <div class="brand"><span class="brand-dot"></span><span class="brand-name">CRESTPRINT</span></div>
      <div class="brand-tag">Printing • Labels • Packaging • Design</div>
    </div>
  </section>

  <!-- Letterhead -->
  <section class="sheet letterhead">
    <div class="brand-block">
      <div class="brand"><span class="brand-dot"></span><span class="brand-name">CRESTPRINT</span></div>
      <div class="brand-tag">Printing • Labels • Packaging • Design</div>
    </div>
    <div class="contact-block">
      <div>Your Address Goes Here<br>City, Zip Code, State<br>Country Name</div>
      <div class="divider"></div>
      <div>
        <div class="contact-line"><span class="contact-icon"></span>123 568 7890</div>
        <div class="contact-line"><span class="contact-icon"></span>123 568 7890</div>
        <div class="contact-line"><span class="contact-icon"></span>123 568 7890</div>
        <div class="contact-line"><span class="contact-icon"></span>name@domainname.com</div>
      </div>
    </div>
    <svg class="footer-wave" width="340" height="80" viewBox="0 0 340 80">
      <path d="M0 18 Q150 60 340 34 L340 80 L0 80Z" fill="var(--blue-light)"/>
      <path d="M0 26 Q150 66 340 44 L340 80 L0 80Z" fill="var(--navy)"/>
    </svg>
    <span class="web">www.crestprint.com</span>
  </section>

  <!-- Envelope -->
  <section class="sheet envelope">
    <svg class="flap" width="710" height="56" viewBox="0 0 710 56" preserveAspectRatio="none">
      <path d="M0 0 L710 0 L710 10 Q355 56 0 10Z" fill="var(--navy)"/>
    </svg>
    <div class="brand-block">
      <div class="brand"><span class="brand-dot"></span><span class="brand-name">CRESTPRINT</span></div>
      <div class="brand-tag">Printing • Labels • Packaging • Design</div>
    </div>
    <div class="address-window"></div>
    <div class="return-address">
      <div class="contact-line"><span class="contact-icon"></span>123 568 7890</div>
      <div class="contact-line"><span class="contact-icon"></span>name@domainname.com</div>
      <div>Your Address Goes Here</div>
      <div>City, Zip Code, State, Country Name</div>
    </div>
  </section>

  <!-- Business card front -->
  <section class="sheet card card-front">
    <div class="brand-block">
      <div class="brand"><span class="brand-dot"></span><span class="brand-name">CRESTPRINT</span></div>
      <div class="brand-tag">Printing • Labels • Packaging • Design</div>
    </div>
    <div class="person">
      <div class="person-name">Dana Merrow <span>| Job Title</span></div>
      <div class="contact-line"><span class="contact-icon"></span>123 568 7890</div>
      <div class="contact-line"><span class="contact-icon"></span>123 568 7890</div>
      <div class="contact-line"><span class="contact-icon"></span>name@domainname.com</div>
    </div>
    <div class="divider"></div>
    <div class="address">Your Address Goes Here<br>City, Zip Code, State<br>Country Name</div>
    <svg class="footer-wave" width="320" height="44" viewBox="0 0 320 44" preserveAspectRatio="none">
      <path d="M0 8 Q140 34 320 14 L320 44 L0 44Z" fill="var(--blue-light)"/>
      <path d="M0 14 Q140 40 320 22 L320 44 L0 44Z" fill="var(--navy)"/>
    </svg>
    <span class="web">www.crestprint.com</span>
  </section>

  <!-- Business card back -->
  <section class="sheet card card-back on-dark">
    <div class="brand-block">
      <div class="brand"><span class="brand-dot"></span><span class="brand-name">CRESTPRINT</span></div>
      <div class="brand-tag">Printing • Labels • Packaging • Design</div>
    </div>
    <span class="web">www.crestprint.com</span>
  </section>

</body>
</html>
```